依頼詳細
作成している原稿があるので別途添付いたします。
記載項目
作成原稿にすべて入れています。
サイズ
A4
ページ数
片面
希望イメージ
シンプル 複雑
単色 カラフル
暗い 明るい
日常 高級
遊び心 厳粛
未来的 伝統的
女性的 男性的
希望する色
無彩色系、無彩色系ですが明るめの色もあれば見たいです
納品ファイル
• イラストレーター形式 (.ai)
• PNG形式 (.png)
補足説明

```html
<!DOCTYPE html>
<html lang="ja">
<head>
<meta charset="utf-8">
<title>えにし学舎群馬校 開校プレ講演会</title>
<link href="https://fonts.googleapis.com/css2?family=Yuji+Syuku&family=Noto+Sans+JP:wght@400;700;900&family=Noto+Serif+JP:wght@700;900&display=swap" rel="stylesheet">
<style>
:root{
  --ink:#0d0d0d;
  --paper:#ffffff;
  --red:#d7141c;
  --grey:#3a3a3a;
  --soft:#bdbdbd;
}
*{margin:0;padding:0;box-sizing:border-box}
html,body{width:846px;height:1200px;overflow:hidden;background:var(--paper)}
.poster{position:relative;width:846px;height:1200px;background:var(--paper);font-family:"Noto Sans JP",sans-serif;color:var(--ink);overflow:hidden}
.hero{position:absolute;left:0;top:0;width:846px;height:690px;background:var(--ink);color:var(--paper)}
.portrait{position:absolute;left:470px;top:30px;width:376px;height:410px;background:radial-gradient(ellipse at 50% 40%,#6a5a4c 0%,#2c2520 45%,#0d0d0d 80%)}
.eyebrow{position:absolute;left:40px;top:20px;font-size:21px;font-weight:700;letter-spacing:2px}
.headline{position:absolute;left:36px;font-family:"Yuji Syuku",serif;line-height:1;white-space:nowrap;text-shadow:0 0 3px #000}
.headline.l1{top:95px;font-size:54px}
.headline.l1 .treasure{color:var(--red)}
.headline.l2{top:175px;font-size:100px}
.headline.l3{top:305px;font-size:84px}
.speaker{position:absolute;left:730px;top:110px;writing-mode:vertical-rl;font-family:"Noto Serif JP",serif;font-weight:900;font-size:76px;line-height:1;letter-spacing:4px;text-shadow:0 0 6px #000}
.speaker-kana{position:absolute;left:706px;top:130px;writing-mode:vertical-rl;font-size:14px;letter-spacing:6px;color:var(--soft)}
.divider{position:absolute;left:0;top:440px;width:846px;height:14px}
.rules-box{position:absolute;left:60px;top:478px;width:320px;height:180px;border:2px solid var(--paper);padding:16px 18px}
.rules-lead{font-size:17px;font-weight:700;line-height:1.45}
.rules-title{display:flex;align-items:baseline;gap:6px;margin-top:10px;white-space:nowrap}
.rules-title .num{font-size:76px;font-weight:900;line-height:.9}
.rules-title .txt{font-family:"Noto Serif JP",serif;font-size:30px;font-weight:900}
.rules-list{position:absolute;left:400px;top:490px;list-style:none;font-size:19px;font-weight:700;line-height:40px;white-space:nowrap}
.rules-list .n{color:var(--red);margin-right:6px}
.rules-list .hl{color:var(--red)}
.overview{position:absolute;left:0;top:700px;width:846px}
.label{position:absolute;left:55px;top:10px;background:var(--ink);color:var(--paper);font-size:20px;font-weight:700;padding:2px 16px}
.label-rule{position:absolute;left:55px;top:22px;width:740px;height:3px;background:var(--ink)}
.row-date{position:absolute;left:55px;top:48px;display:flex;align-items:baseline;gap:16px}
.key{display:inline-block;background:var(--grey);color:var(--paper);font-size:16px;padding:2px 8px}
.date{font-family:"Noto Serif JP",serif;font-weight:900;font-size:34px}
.date .big{font-size:64px;color:var(--red)}
.date .dow{display:inline-block;background:var(--ink);color:var(--paper);font-size:24px;padding:0 4px;margin-left:4px}
.times{position:absolute;left:620px;top:62px;font-size:18px;font-weight:700;line-height:1.5}
.row-venue{position:absolute;left:55px;top:132px;display:flex;align-items:center;gap:16px;width:740px;border-bottom:2px solid var(--ink);padding-bottom:8px}
.venue{font-family:"Noto Serif JP",serif;font-weight:900;font-size:36px}
.addr{margin-left:auto;font-size:14px;line-height:1.4}
.course{position:absolute;left:55px;top:196px;width:740px;border:3px solid var(--red)}
.course-head{display:flex;align-items:center;justify-content:space-between;background:var(--ink);color:var(--paper);padding:6px 12px}
.course-head .t{font-size:22px;font-weight:900}
.course-head .cta{background:var(--red);font-size:26px;font-weight:900;padding:0 14px}
.schedule{width:520px;border-collapse:collapse;margin:6px 0 6px 8px;font-size:16px}
.schedule td{border-bottom:1px solid var(--soft);padding:4px 6px;white-space:nowrap}
.schedule .no{background:var(--grey);color:var(--paper);font-weight:700;text-align:center;width:70px}
.schedule .when{font-weight:700}
.info{position:absolute;right:14px;top:68px;width:180px;color:var(--red);font-weight:700;font-size:16px;line-height:1.45}
.info .big{font-size:22px;color:var(--ink)}
.host{position:absolute;left:0;top:1172px;width:846px;text-align:center;font-size:14px}
</style>
</head>
<body>
<div class="poster">
  <section class="hero">
    <div class="portrait" role="img" aria-label="マイクを持って語る講師の写真"></div>
    <p class="eyebrow">えにし学舎群馬校　開校プレ講演会</p>
    <h1>
      <span class="headline l1">出会いこそ<span class="treasure">宝</span>である</span>
      <span class="headline l2">人のご縁で</span>
      <span class="headline l3">でっかく生きろ</span>
    </h1>
    <p class="speaker-kana">にしかわ かずあき</p>
    <p class="speaker">西川和昭</p>
    <svg class="divider" viewBox="0 0 846 14" preserveAspectRatio="none">
      <polygon points="0,0 846,0 846,14 0,14" fill="#2a2a2a"/>
      <polygon points="0,4 560,4 580,10 0,10" fill="#d7141c"/>
    </svg>
    <div class="rules-box">
      <p class="rules-lead">今日、あなたの心に<br>スイッチが入ります。</p>
      <p class="rules-title"><span class="num">4</span><span class="txt">つの鉄板ルール</span></p>
    </div>
    <ol class="rules-list">
      <li><span class="n">1.</span>返事は<span class="hl">0.2秒</span>!</li>
      <li><span class="n">2.</span>頼まれごとは試されごと!</li>
      <li><span class="n">3.</span>出来ない理由を言わない!</li>
      <li><span class="n">4.</span>そのうちと言わず<span class="hl">今</span>できることを<span class="hl">今</span>やる!</li>
    </ol>
  </section>

  <section class="overview">
    <div class="label-rule"></div>
    <h2 class="label">概要</h2>
    <div class="row-date">
      <span class="key">日時</span>
      <span class="date">2020年<span class="big">7月11日</span><span class="dow">土</span></span>
    </div>
    <p class="times">開演／18時30分より<br>開場／18時00分</p>
    <div class="row-venue">
      <span class="key">会場</span>
      <span class="venue">高崎みどりホール</span>
      <span class="addr">高崎市本町12-3<br>TEL.027-000-1234</span>
    </div>
    <div class="course">
      <div class="course-head">
        <span class="t">えにし学舎群馬校1期　開催予定</span>
        <span class="cta">受講生募集!</span>
      </div>
      <table class="schedule">
        <tr><td class="no">第1講義</td><td class="when">9月6日(日)</td><td>「人に出会って己に出会う」</td><td>西川和昭</td></tr>
        <tr><td class="no">第2講義</td><td class="when">10月3日(土)</td><td>「まく(種まき)ということ」</td><td>山本恵子</td></tr>
        <tr><td class="no">第3講義</td><td class="when">11月7日(土)</td><td>「言葉の力」</td><td>川島知昭</td></tr>
        <tr><td class="no">第4講義</td><td class="when">12月5日(土)</td><td>「足るを知る」</td><td>森田達也</td></tr>
        <tr><td class="no">第5講義</td><td class="when">1月9日(土)</td><td>「プロデュースする」</td><td>中井美保</td></tr>
        <tr><td class="no">第6講義</td><td class="when">2月6日(土)</td><td>「自分の役割を発見」</td><td>西川和昭</td></tr>
      </table>
      <div class="info">
        <p>[開催時間]</p>
        <p class="big">13時～18時</p>
        <p style="margin-top:14px">[開催場所]</p>
        <p class="big">高崎若葉ビル</p>
        <p>徒歩7分</p>
      </div>
    </div>
  </section>
  <p class="host">主催：えにし学舎実行委員会</p>
</div>
</body>
</html>
```